Exclusive beauty salon needs a price list or services booklet

I need a new very attractive flyer for my beauty salon, containing information on the different services and their prices.
In attachment you can find a pdf of the "old" one, but I'd love to have a beautifully designed new one!
I'd love to have a booklet in format 148 x 148 mm, or in US format, containing 12 or 16 pages, but if you can offer other nice looking designs they are welcome!
The services that need to come in the booklet with their prices can all be found on my website: www.atelierkova.be, starting with
Gelaatsverzorging
Wimperverlenging
Suikerontharing
Wimperlifting
Permanente Make Up
Airbrush Tanning

Target Market(s)

woman from 20 to 89 years old

Industry/Entity Type

Beauty Salon

Font styles to use
Sans Serif

Colors

Designer to choose colors to be used in the design.

Requirements
Must have
• a classy nice look, it must contain details about the services from my beauty salon and their prices, and nice pictures.
• The Names, prices and explanations of the services can easily be found on my website: www.atelierkova.be
Nice to have
• In attachment you can find the "old" price list in pdf, what I need now is a "new booklet" with the new logo and updated services price list.
• I need a very nice and attractive looking booklet, classy chique, Paris chique, looking very expensive.
Should not have
• Not too much colors, not too curly, but still feminine

```html
<!DOCTYPE html>
<html lang="nl">
<head>
<meta charset="utf-8">
<title>Atelier Kova – Prijsfolder</title>
<link rel="stylesheet" href="https://fonts.googleapis.com/css2?family=Dosis:wght@300;400;600;700&family=Roboto+Condensed:wght@400;700&family=Poppins:wght@400;500&display=swap">
<style>
:root{
  --stage:#a3a3a3;
  --paper:#f7f7f7;
  --paper-white:#ffffff;
  --teal:#7dd5cb;
  --ink:#1c1c1c;
  --grey-text:#4a4a4a;
  --muted:#777777;
}
*{margin:0;padding:0;box-sizing:border-box}
html,body{width:1200px;height:1200px;overflow:hidden;background:var(--stage)}
body{position:relative;font-family:"Poppins",sans-serif;color:var(--ink)}
.page{position:absolute;background:var(--paper);box-shadow:2px 3px 6px rgba(0,0,0,.35);overflow:hidden}
.page--cover{left:42px;top:38px;width:546px;height:546px}
.page--lashes{left:609px;top:38px;width:539px;height:539px;background:var(--paper-white)}
.page--contact{left:327px;top:609px;width:546px;height:546px}

.brand{position:absolute;text-align:center;font-family:"Dosis",sans-serif;font-weight:300;color:var(--ink);letter-spacing:10px;font-size:20px;white-space:nowrap;transform:translateX(-50%)}

/* cover */
.cover-photo{position:absolute;left:0;top:0;width:300px;height:546px;background:linear-gradient(100deg,#e7c4ae 0%,#f0d3c1 45%,#f3e2d8 80%,rgba(247,247,247,0) 100%)}
.quote-band{position:absolute;left:0;top:247px;width:546px;height:181px;background:var(--teal)}
.quote{position:absolute;right:22px;top:256px;text-align:right;font-family:"Dosis",sans-serif;color:var(--grey-text);text-transform:uppercase}
.quote .l{display:block;font-weight:300;font-size:34px;line-height:37px;letter-spacing:1px}
.quote .b{color:#fff;font-weight:700}
.quote .author{display:block;color:#fff;font-weight:600;font-size:16px;letter-spacing:2.5px;margin-top:4px}

/* lashes */
.lash-photo{position:absolute;left:0;top:0;width:360px;height:216px;background:linear-gradient(110deg,#f1d9ca 0%,#e8c6b2 55%,#f4f0ee 100%)}
.lash-title{position:absolute;left:360px;top:0;width:179px;height:216px;background:var(--teal);text-align:right;padding:42px 22px 0 0;font-family:"Dosis",sans-serif;font-weight:300;color:var(--grey-text);text-transform:uppercase}
.lash-title .s{display:block;font-size:20px;line-height:22px;letter-spacing:1px}
.lash-title .m{display:block;font-size:33px;line-height:30px;letter-spacing:1px}
.lash-title .xl{display:block;color:#fff;font-size:50px;line-height:54px;margin-top:10px;letter-spacing:2px}
.price-row{position:absolute;top:242px;left:64px;display:flex;align-items:center;gap:14px}
.price-label{font-family:"Roboto Condensed",sans-serif;font-weight:700;font-size:13px;line-height:16px;text-transform:uppercase;color:var(--ink)}
.price-tag{background:var(--teal);border-radius:4px;width:83px;height:50px;display:flex;align-items:center;justify-content:center;font-family:"Dosis",sans-serif;font-weight:600;font-size:31px;letter-spacing:2px;color:var(--ink)}
.benefits{position:absolute;left:48px;top:309px}
.benefits h3{font-family:"Poppins",sans-serif;font-weight:500;font-size:10.5px;color:var(--muted);margin-bottom:6px}
.benefits ul{list-style:none}
.benefits li{position:relative;font-size:7.6px;line-height:18px;color:var(--muted);padding-left:11px}
.benefits li::before{content:"";position:absolute;left:0;top:7px;width:5px;height:5px;border-radius:50%;background:var(--ink)}
.lash-footer{position:absolute;left:0;bottom:0;width:539px;height:19px;background:var(--teal)}

/* contact */
.salon-name{position:absolute;top:218px;width:100%;text-align:center;font-family:"Roboto Condensed",sans-serif;font-weight:700;font-size:21px;color:#333;text-transform:uppercase}
.contact-band{position:absolute;left:0;top:248px;width:546px;height:204px;background:var(--teal);color:#fff;font-family:"Roboto Condensed",sans-serif;font-weight:700;font-size:16px}
.contact-band .icon{position:absolute;left:50%;transform:translate(-50%,-50%)}
.contact-band .line{position:absolute;left:0;width:100%;text-align:center;line-height:20px;transform:translateY(-50%)}
.city{position:absolute;top:502px;width:100%;text-align:center;font-family:"Dosis",sans-serif;font-weight:600;font-size:16px;letter-spacing:2px;color:var(--ink)}
</style>
</head>
<body>

<section class="page page--cover">
  <div class="cover-photo" role="img" aria-label="Portret van een vrouw met stralende huid, handen langs het gezicht"></div>
  <div class="brand" style="left:411px;top:152px">ATELIER KOVA</div>
  <div class="quote-band"></div>
  <p class="quote">
    <span class="l">Beauty starts</span>
    <span class="l b">The moment</span>
    <span class="l">You decide to</span>
    <span class="l">Be <span class="b">yourself</span></span>
    <span class="author">Margot Lenaerts</span>
  </p>
</section>

<section class="page page--lashes">
  <div class="lash-photo" role="img" aria-label="Close-up van het aanbrengen van wimperextensions met een pincet"></div>
  <div class="lash-title">
    <span class="s">Individuele</span>
    <span class="m">Wimper</span>
    <span class="s">Verlenging</span>
    <span class="xl">Lumi</span>
    <span class="s">Lash</span>
  </div>
  <div class="price-row">
    <div class="price-label">Erste plaatsing<br>wimperextensions</div>
    <div class="price-tag">€65</div>
    <div class="price-label">Bijwerking na<br>max.4 weken</div>
    <div class="price-tag">€35</div>
  </div>
  <div class="benefits">
    <h3>Voordelen van Lumi Lash Wimperverlenging op een rijtje</h3>
    <ul>
      <li>Pijnloze behandeling</li>
      <li>Geen beschadiging van de natuurlijke wimpers</li>
      <li>Onmiddellijk een verbluffend resultaat</li>
      <li>Geen nazorg</li>
      <li>Verkrijgbaar in verschillende lengtes, diktes en curves</li>
      <li>Prima oplossing voor feestjes, vakanties, enz.</li>
      <li>Mascara wordt overbodig</li>
      <li>Wimperextensions blijven aangehecht tijdens het zwemmen, douchen en saunabezoek</li>
      <li>Lumi Lash garandeert wekenlang plezier</li>
    </ul>
  </div>
  <div class="lash-footer"></div>
</section>

<section class="page page--contact">
  <div class="brand" style="left:273px;top:138px">ATELIER KOVA</div>
  <h2 class="salon-name">Atelier Kova Schoonheidsinstituut</h2>
  <div class="contact-band">
    <svg class="icon" style="top:28px" width="40" height="40" viewBox="0 0 40 40" aria-hidden="true">
      <g fill="none" stroke="#fff" stroke-width="2">
        <rect x="8" y="14" width="8" height="20"/><rect x="17" y="6" width="8" height="28"/><rect x="26" y="16" width="7" height="18"/>
        <line x1="2" y1="36" x2="38" y2="36"/>
      </g>
    </svg>
    <p class="line" style="top:64px">KERKSTRAAT 41 (2E VERD. LINDEGEBOUW)</p>
    <svg class="icon" style="top:98px" width="28" height="28" viewBox="0 0 24 24" aria-hidden="true">
      <path fill="#fff" d="M6.6 10.8a15.1 15.1 0 0 0 6.6 6.6l2.2-2.2a1 1 0 0 1 1-.25 11.4 11.4 0 0 0 3.6.57 1 1 0 0 1 1 1V20a1 1 0 0 1-1 1A17 17 0 0 1 3 4a1 1 0 0 1 1-1h3.5a1 1 0 0 1 1 1c0 1.25.2 2.45.57 3.57a1 1 0 0 1-.25 1z"/>
    </svg>
    <p class="line" style="top:128px">Tel: 0470123456</p>
    <svg class="icon" style="top:158px" width="26" height="22" viewBox="0 0 26 20" aria-hidden="true">
      <rect x="1" y="1" width="24" height="18" fill="none" stroke="#fff" stroke-width="2.5"/>
      <path d="M1 2l12 10L25 2" fill="none" stroke="#fff" stroke-width="2.5"/>
    </svg>
    <p class="line" style="top:184px">Email: info@atelierkova.be</p>
  </div>
  <p class="city">8300 LINDEWIJK</p>
</section>

</body>
</html>
```